Corrindale Planners, LLC Stationary

Corrindale Planners, LLC is a new financial planning and consulting company. We are looking for designs on business cards, letterhead, envelopes, and anything else that would be useful. Our preference for business card design is two sided. We are looking for a professional and clean look with incorporating the logo and patriotic feel. Thank you to all who participate and good luck!

```html
<!DOCTYPE html>
<html lang="en">
<head>
<meta charset="utf-8">
<title>Corrindale Planners, LLC – Business Cards</title>
<link href="https://fonts.googleapis.com/css2?family=Open+Sans:wght@400;600&display=swap" rel="stylesheet">
<style>
  :root {
    --navy: #123f6b;
    --red: #c8202f;
    --paper: #ffffff;
    --stage: #ececec;
    --ink: #2f3540;
  }
  * { margin: 0; padding: 0; box-sizing: border-box; }
  html, body { width: 1200px; height: 917px; overflow: hidden; }
  body {
    background: var(--stage);
    font-family: "Open Sans", Arial, sans-serif;
    position: relative;
  }
  .card {
    position: absolute;
    top: 320px;
    width: 490px;
    height: 280px;
    box-shadow: 0 10px 30px rgba(0,0,0,0.12);
    overflow: hidden;
  }
  .card-front { left: 80px; background: var(--navy); }
  .card-back { left: 630px; background: var(--paper); }

  .brand {
    position: absolute;
    display: flex;
    align-items: center;
    gap: 10px;
  }
  .brand-mark {
    width: 18px; height: 18px; border-radius: 50%;
    flex: none;
  }
  .brand-name {
    font-weight: 600;
    font-size: 22px;
    letter-spacing: 0.5px;
    white-space: nowrap;
  }
  .brand-tagline {
    position: absolute;
    font-size: 8px;
    letter-spacing: 1.6px;
    text-transform: uppercase;
    white-space: nowrap;
  }
  .card-front .brand { left: 0; right: 0; top: 112px; justify-content: center; }
  .card-front .brand-mark { background: var(--paper); }
  .card-front .brand-name { color: var(--paper); }
  .card-front .brand-tagline { left: 0; right: 0; top: 148px; text-align: center; color: var(--paper); }

  .card-back .brand { right: 26px; top: 36px; }
  .card-back .brand-mark { background: var(--red); }
  .card-back .brand-name { color: var(--navy); font-size: 18px; }
  .card-back .brand-tagline { right: 26px; top: 66px; color: var(--navy); font-size: 7px; }

  .holder { position: absolute; left: 28px; top: 70px; }
  .holder-name { color: var(--navy); font-weight: 600; font-size: 17px; }
  .holder-role { color: var(--red); font-size: 13px; margin-top: 1px; }
  .holder-address { color: var(--ink); font-size: 11px; line-height: 1.45; margin-top: 10px; }

  .contact {
    position: absolute; right: 26px; top: 152px;
    list-style: none; text-align: right;
  }
  .contact li {
    display: flex; justify-content: flex-end; align-items: center;
    gap: 8px; color: var(--ink); font-size: 11px; line-height: 21px;
  }
  .contact svg { width: 12px; height: 12px; fill: var(--navy); flex: none; }

  .card-bands { position: absolute; left: 0; bottom: 0; width: 490px; height: 60px; }
</style>
</head>
<body>

<section class="card card-front" aria-label="Business card front">
  <div class="brand">
    <span class="brand-mark"></span>
    <span class="brand-name">CORRINDALE PLANNERS, LLC</span>
  </div>
  <p class="brand-tagline">Financial Planning and Consulting</p>
</section>

<section class="card card-back" aria-label="Business card back">
  <div class="brand">
    <span class="brand-mark"></span>
    <span class="brand-name">CORRINDALE PLANNERS, LLC</span>
  </div>
  <p class="brand-tagline">Financial Planning and Consulting</p>

  <div class="holder">
    <p class="holder-name">Daniel Harlow</p>
    <p class="holder-role">Financial Advisor</p>
    <p class="holder-address">418 Brookfield Ave # 120, Larkston,<br>GA 30199, USA</p>
  </div>

  <ul class="contact">
    <li>+1 555-014-2290
      <svg viewBox="0 0 24 24"><path d="M6.6 10.8a15 15 0 0 0 6.6 6.6l2.2-2.2a1 1 0 0 1 1-.25 11.4 11.4 0 0 0 3.6.57 1 1 0 0 1 1 1V20a1 1 0 0 1-1 1A17 17 0 0 1 3 4a1 1 0 0 1 1-1h3.5a1 1 0 0 1 1 1c0 1.25.2 2.45.57 3.6a1 1 0 0 1-.25 1z"/></svg>
    </li>
    <li>info@CorrindalePlanners.com
      <svg viewBox="0 0 24 24"><path d="M2 5h20v14H2z M3 6l9 7 9-7" fill="none" stroke="#123f6b" stroke-width="2"/></svg>
    </li>
    <li>www.CorrindalePlanners.com
      <svg viewBox="0 0 24 24"><circle cx="12" cy="12" r="9" fill="none" stroke="#123f6b" stroke-width="2"/><path d="M3 12h18M12 3c3 3 3 15 0 18M12 3c-3 3-3 15 0 18" fill="none" stroke="#123f6b" stroke-width="1.6"/></svg>
    </li>
  </ul>

  <svg class="card-bands" viewBox="0 0 490 60" preserveAspectRatio="none" aria-hidden="true">
    <polygon points="0,28 210,28 200,44 0,44" fill="var(--navy)"/>
    <polygon points="214,28 490,28 490,44 204,44" fill="var(--red)"/>
  </svg>
</section>

</body>
</html>
```